New webpage for Facility Management Company (cleaning services)

We need a new web page design for a company based in Stockholm, Sweden, called TKR Clean AB (established 1991). We provide cleaning services to the public sector, to businesses, and to home owners. Our services primarily include daily cleaning, floor care, window cleaning, and carpet cleaning.

Our company holds certificates for ISO 9001, ISO 14001, ISO 45001 and "Hjorten".

Referring to "the Swedish model" we honor collective agreements between Veltrio (employer-representative organisation and relevant labour unions (e.g. Arbetsfront).
The final design should communicate that we are a trustworthy company with a well trained staff, high quality services combined with a commitment to run a sustainable business from a labour and environmental perspective.

DETAILS
General
-----------------------------------------------
• Language: Swedish (we provide text)
• Very important: Easy to administrate for company staff without special technical skills, especially to
o add/change information about HQ staff
o change any text
o add/change information about offered services
• Responsive
• SEO-friendly

Content that web page needs to cover in one way or the other
--------------------------------------------
• Information about our company
• About our staff and contact info to HQstaff/management (photos, contact info)
• Our ambitions and supporting info (quality, environment, labour conditions, certificates, etc)
• Information to customers within the public sector
• Information to customers within the private sector
• Information to customers within the home owner sector
• Services public sector (Swedish = Offentlig sektor)
• Services private business sector (Swedish = Företag) Se törnvall
• Services home owner sector (Swedish=Privat)
• GDPR compliance
• News

Content/Function
-------------------------------
• One specific requirement is that we need a page for information to potentially new employees (some general information and open job positions) with a possibility to fill in a simple application form and upload CV.(Mail?) CAPTCHA or equivalent.
• Contact form for customers with CAPTCHA or equivalent.
• Cookie management
• Integration social media (future); easy to manage/add/delete integration of social media.

We are not interested in a blog at this point of time

```html
<!DOCTYPE html>
<html lang="sv">
<head>
<meta charset="utf-8">
<title>TKR Clean AB – Städföretaget i Stockholm</title>
<link rel="stylesheet" href="https://fonts.googleapis.com/css2?family=Lora:wght@400;700&family=Arimo:wght@400;700&display=swap">
<style>
:root{
  --green:#4cb848;
  --blue:#0b8fd9;
  --teal:#1aa3a0;
  --dark:#1b1b1b;
  --text:#555;
  --heading:#333;
  --light:#f4f5f7;
  --white:#fff;
}
*{box-sizing:border-box;margin:0;padding:0}
html,body{width:1200px;height:4386px;overflow:hidden}
body{position:relative;font-family:"Arimo",Arial,sans-serif;color:var(--text);background:var(--white)}
.abs{position:absolute}

/* header */
.site-header{position:absolute;top:0;left:0;width:1200px;height:120px;border-top:4px solid var(--green)}
.brand-name{position:absolute;left:112px;top:50px;font-family:"Arimo",Arial,sans-serif;font-weight:700;font-size:24px;letter-spacing:.5px;color:var(--heading)}
.main-nav{position:absolute;left:440px;top:58px;display:flex;gap:22px;font-family:"Lora",Georgia,serif;font-size:13px;color:#333;text-transform:uppercase}
.main-nav .active{color:var(--green)}
.caret::after{content:"";display:inline-block;margin-left:4px;border:4px solid transparent;border-top-color:#333;vertical-align:-2px}
.search-btn{position:absolute;left:1040px;top:42px;width:48px;height:48px;border-radius:50%;background:var(--green);display:flex;align-items:center;justify-content:center}

/* hero */
.hero{position:absolute;top:120px;left:0;width:1200px;height:790px}
.hero-copy{position:absolute;left:112px;top:230px;color:var(--white)}
.hero-kicker{font-family:"Lora",Georgia,serif;font-size:26px}
.hero-title{font-family:"Lora",Georgia,serif;font-size:58px;font-weight:700;margin-top:4px;letter-spacing:1px}
.hero-lead{font-family:"Lora",Georgia,serif;font-size:19px;line-height:34px;margin-top:18px}
.btn-outline{display:inline-flex;align-items:center;justify-content:center;border:2px solid var(--white);border-radius:30px;color:var(--white);font-family:"Lora",Georgia,serif;font-weight:700;text-transform:uppercase}
.hero .btn-outline{margin-top:34px;width:171px;height:60px;font-size:16px;background:var(--blue)}

.section-title{position:absolute;left:0;width:1200px;text-align:center;font-family:"Lora",Georgia,serif;font-weight:400;font-size:34px;color:var(--heading);text-transform:uppercase}
.section-title::after{content:"";display:block;width:70px;height:3px;background:var(--blue);margin:14px auto 0}

/* ambitions */
.ambition{position:absolute;top:1083px;width:229px;height:391px;border-radius:8px;color:var(--white);text-align:center;padding-top:42px}
.ambition.green{background:var(--green)}
.ambition.blue{background:var(--blue)}
.ambition h3{font-family:"Lora",Georgia,serif;font-size:19px;font-weight:700;margin-top:16px}
.ambition h3::after{content:"";display:block;width:26px;height:2px;background:var(--white);margin:12px auto 0}
.ambition p{font-size:13px;line-height:25px;padding:0 18px;margin-top:18px}
.ambition .btn-outline{margin-top:18px;width:132px;height:44px;font-size:13px}

/* about */
.about{position:absolute;top:1540px;left:0;width:1200px;height:720px}
.about-circle{position:absolute;left:102px;top:120px;width:510px;height:510px;border-radius:50%;background:var(--green);border:12px solid var(--blue);color:var(--white);text-align:center;padding:62px 50px 0 60px}
.about-circle h2{font-family:"Lora",Georgia,serif;font-weight:400;font-size:44px}
.about-circle .sub{font-family:"Lora",Georgia,serif;font-size:15px;margin-top:6px}
.about-list{list-style:none;text-align:left;margin-top:20px}
.about-list li{position:relative;padding-left:24px;font-size:14px;line-height:26px;margin-bottom:12px}
.about-list li::before{content:"";position:absolute;left:0;top:6px;width:11px;height:11px;border:1.5px solid var(--white);border-radius:50%}

/* news */
.news-card{position:absolute;top:2395px;width:310px;height:478px;border:1px solid #e3e3e3;border-radius:6px;background:var(--white);text-align:center;box-shadow:0 1px 4px rgba(0,0,0,.06)}
.news-photo{height:254px;border-radius:6px 6px 0 0}
.news-date{position:absolute;left:111px;top:210px;width:88px;height:88px;border-radius:50%;background:var(--green);color:var(--white);font-family:"Lora",Georgia,serif;line-height:1}
.news-date b{display:block;font-size:34px;font-weight:400;margin-top:12px}
.news-date span{font-size:18px}
.news-card h3{font-family:"Lora",Georgia,serif;font-weight:400;font-size:21px;line-height:28px;color:var(--heading);margin-top:58px;padding:0 40px}
.news-card p{font-size:13px;line-height:25px;padding:0 22px;margin-top:14px}

/* staff */
.staff-band{position:absolute;top:2953px;left:0;width:1200px;height:545px;background:var(--light)}
.staff{position:absolute;top:3078px;width:300px;text-align:center}
.staff-photo{width:186px;height:186px;border-radius:50%;margin:0 auto}
.staff h3{font-family:"Lora",Georgia,serif;font-size:19px;font-weight:700;color:var(--heading);margin-top:24px}
.staff p{font-size:13px;line-height:25px;margin-top:10px;padding:0 30px}
.staff .phone{color:var(--blue);font-family:"Lora",Georgia,serif;font-size:14px;margin-top:14px}

/* info */
.info{position:absolute;top:3498px;height:470px;width:600px;color:var(--white);padding:88px 0 0 112px}
.info.left{left:0;background:linear-gradient(135deg,#5dbf55,#3fa646)}
.info.right{left:600px;background:linear-gradient(135deg,#0c92dc,#0a86d0);padding-left:53px}
.info h2{font-family:"Lora",Georgia,serif;font-size:25px;font-weight:700}
.info ul{list-style:none;margin-top:20px}
.info li{position:relative;padding-left:32px;font-family:"Lora",Georgia,serif;font-size:17px;line-height:46px}
.info li::before{content:"";position:absolute;left:0;top:15px;width:14px;height:14px;border:1.5px solid var(--white);border-radius:50%}
.info .btn-outline{margin-top:24px;width:164px;height:58px;font-size:17px;background:transparent}

/* footer */
.site-footer{position:absolute;top:3860px;left:0;width:1200px;height:526px}
.footer-heading{font-family:"Lora",Georgia,serif;font-size:20px;font-weight:700;color:var(--white);text-transform:uppercase;letter-spacing:.5px}
.field{position:absolute;height:34px;background:var(--white);font-size:13px;color:#444;padding:9px 10px}
.captcha{position:absolute;left:112px;top:356px;width:170px;height:42px;background:#f9f9f9;border:1px solid #ccc;border-radius:3px;font-size:9px;color:#333;display:flex;align-items:center;padding-left:8px;gap:8px}
.captcha i{width:14px;height:14px;border:1px solid #999;background:var(--white)}
.send-btn{position:absolute;left:300px;top:360px;width:117px;height:36px;border-radius:20px;background:var(--blue);color:var(--white);font-family:"Lora",Georgia,serif;font-weight:700;font-size:14px;display:flex;align-items:center;justify-content:center}
.contact-item{position:absolute;left:556px;display:flex;gap:14px;color:var(--white)}
.contact-icon{width:44px;height:44px;border:1.5px solid var(--white);border-radius:50%;display:flex;align-items:center;justify-content:center;flex:none}
.contact-item strong{display:block;font-family:"Lora",Georgia,serif;font-weight:400;font-size:17px;text-transform:uppercase}
.contact-item span{font-size:13px;line-height:19px}
.footer-name{position:absolute;left:806px;top:250px;width:280px;text-align:center;font-family:"Arimo",Arial,sans-serif;font-weight:700;font-size:24px;letter-spacing:.5px;color:var(--white)}
.badge{position:absolute;top:400px;width:56px;height:56px;border-radius:50%}
.copyright{position:absolute;left:0;top:472px;width:1200px;text-align:center;font-family:"Lora",Georgia,serif;font-size:15px;color:var(--white)}
.version{position:absolute;left:1094px;top:466px;font-size:15px;color:var(--white)}
</style>
</head>
<body>

<header class="site-header">
  <div class="brand-name">TKR Clean AB</div>
  <nav class="main-nav">
    <span class="active">Hem</span>
    <span class="caret">Om oss</span>
    <span>Tjänsteutbud</span>
    <span class="caret">Kontakt</span>
    <span class="caret">Anställda</span>
    <span>Ärendehantering</span>
  </nav>
  <div class="search-btn">
    <svg width="16" height="16" viewBox="0 0 16 16" fill="none" stroke="#fff" stroke-width="2.2"><circle cx="6.5" cy="6.5" r="4.5"/><path d="M10 10l4 4"/></svg>
  </div>
</header>

<section class="hero">
  <svg class="abs" width="1200" height="790" viewBox="0 0 1200 790" role="img" aria-label="Städmiljö i grön och blå ton bakom välkomsttexten">
    <defs>
      <linearGradient id="heroGrad" x1="0" y1="0" x2="1" y2="0.3">
        <stop offset="0" stop-color="#47b64a"/>
        <stop offset="0.5" stop-color="#2ea88a"/>
        <stop offset="1" stop-color="#1196c9"/>
      </linearGradient>
      <linearGradient id="curveGrad" x1="0" x2="1">
        <stop offset="0" stop-color="#4cb848"/>
        <stop offset="1" stop-color="#0b8fd9"/>
      </linearGradient>
    </defs>
    <path d="M0 0H1200V610C950 800 350 800 0 660Z" fill="url(#heroGrad)"/>
    <path d="M0 660C350 800 950 800 1200 610V622C950 812 350 812 0 672Z" fill="url(#curveGrad)"/>
  </svg>
  <div class="abs" role="img" aria-label="Fönsterputsare i gula handskar, inramad i vit ram"
       style="left:672px;top:40px;width:400px;height:640px;border-radius:50% 50% 48% 48% / 40% 40% 60% 60%;border:6px solid #fff;background:linear-gradient(160deg,#8fc78a,#d8cfc0 55%,#e9d36a)"></div>
  <div class="hero-copy">
    <div class="hero-kicker">VÄLKOMMEN TILL</div>
    <div class="hero-title">TKR CLEAN AB</div>
    <p class="hero-lead">Städföretaget där kvaliteten alltid är högre än priset!<br>Vi har 30 års erfarenhet!</p>
    <span class="btn-outline">Läs mer</span>
  </div>
  <svg class="abs" style="left:570px;top:738px" width="60" height="16">
    <circle cx="12" cy="8" r="7" fill="#fff"/><circle cx="30" cy="8" r="7" fill="#555"/><circle cx="48" cy="8" r="7" fill="#fff"/>
  </svg>
</section>

<h2 class="section-title" style="top:974px">Våra ambitioner</h2>

<article class="ambition green" style="left:111px">
  <svg width="84" height="84" viewBox="0 0 84 84" fill="none" stroke="#fff" stroke-width="2.4"><circle cx="42" cy="34" r="22"/><circle cx="42" cy="34" r="13"/><path d="M28 50L20 74l10-4 6 8 6-22M56 50l8 24-10-4-6 8-6-22"/></svg>
  <h3>KVALITET</h3>
  <p>Sed ut perspiciatis unde omnis iste natus error sit voluptatem accusantium doloremque laud dicta sunt explicabo.</p>
  <span class="btn-outline">Lär dig mer</span>
</article>
<article class="ambition blue" style="left:361px">
  <svg width="84" height="84" viewBox="0 0 84 84" fill="none" stroke="#fff" stroke-width="2.4"><path d="M42 18c10 8 10 22 0 30-10-8-10-22 0-30zM42 48V30"/><path d="M12 40v18l16 16v8M72 40v18L56 74v8M20 44l12 14M64 44L52 58"/></svg>
  <h3>MILJÖ</h3>
  <p>Sed ut perspiciatis unde omnis iste natus error sit voluptatem accusantium doloremque laud dicta sunt explicabo.</p>
  <span class="btn-outline">Lär dig mer</span>
</article>
<article class="ambition green" style="left:609px">
  <svg width="84" height="84" viewBox="0 0 84 84" fill="none" stroke="#fff" stroke-width="2.4"><circle cx="40" cy="28" r="12"/><path d="M26 22h28M16 78V64c0-10 10-16 24-16s24 6 24 16v14"/><path d="M58 36l14-14M66 20a5 5 0 1 0 8 6"/></svg>
  <h3>ARBETSVILLKOR</h3>
  <p>Sed ut perspiciatis unde omnis iste natus error sit voluptatem accusantium doloremque laud dicta sunt explicabo.</p>
  <span class="btn-outline">Lär dig mer</span>
</article>
<article class="ambition blue" style="left:860px">
  <svg width="84" height="84" viewBox="0 0 84 84" fill="none" stroke="#fff" stroke-width="2.4"><path d="M22 10h30l12 12v52H22z"/><path d="M52 10v12h12M30 34h22M30 44h18M30 54h14"/><circle cx="58" cy="60" r="8"/></svg>
  <h3>CERTIFIKAT</h3>
  <p>Sed ut perspiciatis unde omnis iste natus error sit voluptatem accusantium doloremque laud dicta sunt explicabo.</p>
  <span class="btn-outline">Lär dig mer</span>
</article>

<section class="about">
  <svg class="abs" width="1200" height="720" viewBox="0 0 1200 720" role="img" aria-label="Städerska som dammsuger golvet i ett ljust vardagsrum">
    <defs>
      <linearGradient id="roomGrad" x1="0" x2="1">
        <stop offset="0" stop-color="#f2f3f4"/>
        <stop offset="0.6" stop-color="#dcdcd8"/>
        <stop offset="1" stop-color="#c9c8c0"/>
      </linearGradient>
    </defs>
    <path d="M0 80C300 -10 900 -20 1200 40V570C900 720 300 710 0 620Z" fill="url(#roomGrad)"/>
    <path d="M0 80C300 -10 900 -20 1200 40V30C900 -30 300 -22 0 68Z" fill="#4cb848"/>
    <path d="M0 620C300 710 900 720 1200 570V582C900 732 300 722 0 632Z" fill="#1aa3a0"/>
  </svg>
  <div class="about-circle">
    <h2>OM OSS</h2>
    <div class="sub">TKR CLEAN AB – EN KORT PRESENTATION</div>
    <ul class="about-list">
      <li>TKR Clean är ett lokalvårdsföretag med städning av skolor, kontor, trappor, lägenheter mm.</li>
      <li>Vi utför även golvvård, storstädning, fönsterputs, storstädning, flyttstädning, mm.</li>
      <li>TKR Clean har lång erfarenhet med stor kompetens. Vi har ca 250 anställda.</li>
      <li>Våra kunder finns i Storstockholm inom den offentliga och privata sektorn.</li>
    </ul>
  </div>
</section>

<h2 class="section-title" style="top:2305px">Senaste nytt</h2>

<article class="news-card" style="left:111px">
  <div class="news-photo" role="img" aria-label="Städpersonal torkar bord och golv" style="background:linear-gradient(135deg,#e8e4dc,#b8c2b6 60%,#d9c65a)"></div>
  <div class="news-date"><b>09</b><span>NOV</span></div>
  <h3>Men för att se var det kommer ifrån</h3>
  <p>Nemo enim ipsam voluptatem quia voluptas sit aspernatur aut odit aut fugit eos qui ratione voluptatem</p>
</article>
<article class="news-card" style="left:444px">
  <div class="news-photo" role="img" aria-label="Golvmopp och blå hink på kontorsgolv" style="background:linear-gradient(160deg,#9cb6c7,#6f8fa8 55%,#c7cbcf)"></div>
  <div class="news-date"><b>09</b><span>NOV</span></div>
  <h3>Men för att se var det kommer ifrån</h3>
  <p>Nemo enim ipsam voluptatem quia voluptas sit aspernatur aut odit aut fugit eos qui ratione voluptatem</p>
</article>
<article class="news-card" style="left:778px">
  <div class="news-photo" role="img" aria-label="Mattrengöring med gula handskar" style="background:linear-gradient(150deg,#efefec,#d4d3cf 50%,#e8d060)"></div>
  <div class="news-date"><b>09</b><span>NOV</span></div>
  <h3>Men för att se var det kommer ifrån</h3>
  <p>Nemo enim ipsam voluptatem quia voluptas sit aspernatur aut odit aut fugit eos qui ratione voluptatem</p>
</article>

<section class="staff-band"></section>
<h2 class="section-title" style="top:2981px">Om vår personal</h2>

<article class="staff" style="left:126px">
  <div class="staff-photo" role="img" aria-label="Porträtt av anställd i blått förkläde" style="background:linear-gradient(160deg,#d9dde2,#3b78b5 70%,#e6cf45)"></div>
  <h3>JONAS BERG</h3>
  <p>Sed ut perspiciatis unde omnis iste natus error sit voluptatem accusantium dolorem laudantium, totam rem</p>
  <div class="phone">✆ | +46 70 000 00 00</div>
</article>
<article class="staff" style="left:456px">
  <div class="staff-photo" role="img" aria-label="Porträtt av anställd i köksmiljö" style="background:linear-gradient(160deg,#e3e5e2,#a9b8a4 60%,#e3d24d)"></div>
  <h3>JONAS BERG</h3>
  <p>Sed ut perspiciatis unde omnis iste natus error sit voluptatem accusantium dolorem laudantium, totam rem</p>
  <div class="phone">✆ | +46 70 000 00 00</div>
</article>
<article class="staff" style="left:784px">
  <div class="staff-photo" role="img" aria-label="Porträtt av anställd i blå skjorta på kontor" style="background:linear-gradient(160deg,#e0e4ea,#2f6fc4 60%,#c7cdd6)"></div>
  <h3>JONAS BERG</h3>
  <p>Sed ut perspiciatis unde omnis iste natus error sit voluptatem accusantium dolorem laudantium, totam rem</p>
  <div class="phone">✆ | +46 70 000 00 00</div>
</article>

<section class="info left">
  <h2>INFORMATION TILL KUNDER</h2>
  <ul>
    <li>Information till kunder inom offentlig sektor</li>
    <li>Information till kunder inom den privata sektorn</li>
    <li>Information till kunder inom villaägarsektorn</li>
  </ul>
  <span class="btn-outline">Läs mer</span>
</section>
<section class="info right">
  <h2>TJÄNSTER OFFENTLIG SEKTOR</h2>
  <ul>
    <li>Tjänster offentlig sektor</li>
    <li>Tjänster privat näringsliv</li>
    <li>Tjänster husägare sektor</li>
  </ul>
  <span class="btn-outline">Läs mer</span>
</section>

<footer class="site-footer">
  <svg class="abs" width="1200" height="526" viewBox="0 0 1200 526"><path d="M0 0L1200 97V526H0Z" fill="var(--dark)"/></svg>
  <h3 class="footer-heading abs" style="left:112px;top:148px">Komma i kontakt</h3>
  <div class="field" style="left:112px;top:200px;width:181px">Förnamn</div>
  <div class="field" style="left:303px;top:200px;width:181px">Efternamn</div>
  <div class="field" style="left:112px;top:243px;width:181px">E-post</div>
  <div class="field" style="left:303px;top:243px;width:181px">Telefon</div>
  <div class="field" style="left:112px;top:286px;width:372px;height:54px">Meddelande</div>
  <div class="captcha"><i></i>Jag är ingen robot</div>
  <div class="send-btn">SKICKA IN</div>

  <h3 class="footer-heading abs" style="left:565px;top:148px">Kontakt</h3>
  <div class="contact-item" style="top:196px">
    <div class="contact-icon"><svg width="14" height="18" viewBox="0 0 14 18" fill="#fff"><path d="M7 0a7 7 0 0 0-7 7c0 5 7 11 7 11s7-6 7-11a7 7 0 0 0-7-7zm0 10a3 3 0 1 1 0-6 3 3 0 0 1 0 6z"/></svg></div>
    <div><strong>Adress</strong><span>Ängsvägen 12, 128 40<br>Sköndal</span></div>
  </div>
  <div class="contact-item" style="top:270px">
    <div class="contact-icon"><svg width="16" height="16" viewBox="0 0 16 16" fill="#fff"><path d="M3 1l3 3-1.5 2a9 9 0 0 0 5.5 5.5L12 10l3 3-2 2.5C7 15 1 9 .5 3z"/></svg></div>
    <div><strong>Telefon</strong><span>08-123 45 67</span></div>
  </div>
  <div class="contact-item" style="top:338px">
    <div class="contact-icon"><svg width="16" height="12" viewBox="0 0 16 12" fill="#fff"><path d="M0 0h16v2L8 7 0 2zM0 4l8 5 8-5v8H0z"/></svg></div>
    <div><strong>E-post</strong><span>info@tkrclean.se</span></div>
  </div>

  <div class="footer-name">TKR Clean AB</div>
  <div class="badge" style="left:806px;background:#2f7fc1"></div>
  <div class="badge" style="left:872px;background:#6ab43e"></div>
  <div class="badge" style="left:948px;background:#55b14a"></div>
  <div class="badge" style="left:1030px;background:#2d8a4c"></div>

  <div class="copyright">© Copyright 2022 TKR Clean.Alla rättigheter reserverade</div>
  <div class="version">C2</div>
</footer>

</body>
</html>
```